Letterhead for SaaS

Design a letterhead that aligns with our new business card, using our logo and color scheme and text defined in the Branding Guide to ensure consistency. Consider incorporating a subtle watermark for added elegance. The layout should reflect the card's style, creating a cohesive look across our stationery.

```html
<!DOCTYPE html>
<html lang="en">
<head>
<meta charset="utf-8">
<title>Novaris Letterhead</title>
<link rel="stylesheet" href="https://fonts.googleapis.com/css2?family=Lato:wght@400;700&family=Montserrat:wght@400;600;700&family=Tangerine:wght@700&display=swap">
<style>
  :root{
    --bg:#e3e3e3;
    --paper:#f4f4f5;
    --navy:#141c33;
    --navy-deep:#0d1326;
    --brand:#4d6bb3;
    --sky:#3fb9e3;
    --ink:#333333;
    --white:#ffffff;
  }
  *{box-sizing:border-box;margin:0;padding:0}
  html,body{width:1153px;height:1200px;overflow:hidden;background:var(--bg)}
  .letterhead{
    position:absolute;left:183px;top:50px;width:786px;height:1100px;
    background:radial-gradient(ellipse at 60% 25%, #fbfbfc 0%, var(--paper) 60%, #ececee 100%);
    overflow:hidden;box-shadow:0 10px 30px rgba(0,0,0,.18);
    font-family:'Lato',sans-serif;color:var(--ink);
  }
  .header{
    position:absolute;left:0;top:0;width:100%;height:213px;
    background:linear-gradient(125deg,var(--navy-deep) 0%,#1b2544 35%,var(--navy) 60%,#18223f 80%,var(--navy-deep) 100%);
  }
  .brand{position:absolute;left:118px;top:136px;display:flex;align-items:center;gap:10px}
  .brand-mark{width:14px;height:14px;background:var(--brand)}
  .brand-name{font-family:'Montserrat',sans-serif;font-weight:700;font-size:26px;letter-spacing:1px;color:var(--brand)}
  .contact{
    position:absolute;left:543px;top:60px;padding-left:13px;
    border-left:1px solid var(--sky);
    font-family:'Montserrat',sans-serif;color:var(--white);font-size:13px;line-height:17px;
  }
  .contact-name{font-weight:600;font-size:13.5px}
  .contact-role{margin-bottom:5px}
  .contact-line{display:flex;align-items:center;gap:8px}
  .contact-line svg{width:10px;height:10px;fill:var(--sky)}
  .watermark{
    position:absolute;left:236px;top:334px;width:360px;height:360px;border-radius:50%;
    background:radial-gradient(circle,rgba(205,207,214,.35) 0%,rgba(205,207,214,.15) 60%,rgba(205,207,214,0) 100%);
  }
  .body{position:absolute;left:60px;top:263px;width:666px;font-size:14.6px;line-height:17px}
  .lead{font-size:15.5px;line-height:18px}
  .date{margin-bottom:19px}
  .recipient{margin-bottom:17px}
  .address{margin-bottom:22px}
  .salutation{font-weight:700;font-size:19.5px;line-height:22px;margin-bottom:19px}
  .body p.copy{text-align:justify;margin-bottom:16px}
  .closing{margin-top:36px;font-size:15px}
  .signature{font-family:'Tangerine',cursive;font-weight:700;font-size:46px;line-height:1;margin-top:12px;margin-left:4px;color:#222}
  .footer{position:absolute;left:0;bottom:0;width:786px;height:143px}
</style>
</head>
<body>
<div class="letterhead">
  <header class="header" role="img" aria-label="Dark navy faceted geometric background">
    <div class="brand">
      <span class="brand-mark"></span>
      <span class="brand-name">NOVARIS</span>
    </div>
    <div class="contact">
      <div class="contact-name">Adrian M. Vale</div>
      <div class="contact-role">Founder + CEO</div>
      <div class="contact-line"><svg viewBox="0 0 10 10"><path d="M1 4c0-2 2-3 4-3s4 1 4 3H7V3H3v1zM2 5h6l1 4H1z"/></svg>(555) 014-2287</div>
      <div class="contact-line"><svg viewBox="0 0 10 10"><path d="M0 2h10v6H0zM0 2l5 3 5-3" stroke="#141c33" stroke-width=".8"/></svg>adrian.v@novaris.io</div>
      <div class="contact-line"><svg viewBox="0 0 10 10"><circle cx="5" cy="5" r="4.5"/></svg>www.novaris.io</div>
    </div>
  </header>

  <div class="watermark" role="img" aria-label="Faint brand watermark"></div>

  <main class="body">
    <p class="lead date">Feb-03-2022</p>
    <p class="lead recipient">Mr, John Doe<br>President</p>
    <p class="lead address">Harbor Systems<br>123 Street Name, Suite# 10<br>City, State, 120023</p>
    <p class="salutation">Dear Mr, John</p>
    <p class="copy">Lorem ipsum dolor sit amet, consectetur adipisicing elit, sed do eiusmod tempor incididunt ut labore et dolore magna aliqua. Ut enim ad minim veniam, quis nostrud exercitation ullamco laboris nisi ut aliquip ex ea commodo consequat. Duis aute irure dolor in reprehenderit in voluptate velit esse cillum dolore eu fugiat nulla pariatur.</p>
    <p class="copy">Lorem ipsum dolor sit amet, consectetur adipisicing elit, sed do eiusmod tempor incididunt ut labore et dolore magna aliqua. Ut enim ad minim veniam, quis nostrud exercitation ullamco laboris nisi ut aliquip ex ea commodo consequat. Duis aute irure dolor in reprehenderit in voluptate velit esse cillum dolore eu fugiat nulla pariatur.</p>
    <p class="copy">Lorem ipsum dolor sit amet, consectetur adipisicing elit, sed do eiusmod tempor incididunt ut labore et dolore magna aliqua. Ut enim ad minim veniam, quis nostrud exercitation ullamco laboris nisi ut aliquip ex ea commodo consequat.</p>
    <p class="copy">Excepteur sint occaecat cupidatat non proident, sunt in culpa qui officia deserunt mollit anim id est laborum. re et dolore magnam aliquam quaerat voluptatem.</p>
    <p class="closing">Regards</p>
    <p class="signature">Daniel Hart</p>
  </main>

  <svg class="footer" viewBox="0 0 1068 194" preserveAspectRatio="none" aria-hidden="true">
    <path d="M0 0 C240 105 560 200 940 97 C600 215 250 145 0 60 Z" fill="var(--sky)"/>
    <path d="M0 68 C280 165 560 175 720 100 C790 70 840 40 880 40 C960 40 1020 70 1068 92 V194 H0 Z" fill="var(--navy)"/>
  </svg>
</div>
</body>
</html>
```